Tideward Fuel Product design

We need a bottle design for our product. Tideward Fuel is a Gaming Nootropic made to increase Energy, Focus, Reaction time, and Clarity of an eSport gamer. It will be 40 servings a bottle. Currently, all the ingredients haven't been finalized so after the competition is over we will have to work with the designer to also make an ingredients label for the back of it. For the flavor, we will call it ember dusk.

The attachments included:. The velvet mongoose picture as a font style I like for the logo.
The K BOLT SURGEWAVE PICTURE IS WHAT WE WANT OUR DESIGN to look like something similar a clean and simple design that stands out!

K Bolt bottle is what our biggest competitors product looks like. The tideward fuel picture as the current logo we are using but can be changed.

Overall the pictures are just some references for what I could possibly want the design to look like however, I'm open to your designer's ideas and concepts you think would make for a cool looking Gaming Nootropic product bottle design. I appreciate everyone working on this and look forward to seeing your designs have a great day!

Target Market(s)

Gamers between the ages of 18-30

Industry/Entity Type

Health And Wellness

Requirements
Must have
• Tideward Fuel logo, state that it is for energy, focus, reaction, and clarity. state 40 serivngs. state flavor.

```html
<!DOCTYPE html>
<html lang="en">
<head>
<meta charset="utf-8">
<title>Tideward Fuel – Ember Dusk Label</title>
<link href="https://fonts.googleapis.com/css2?family=Montserrat:wght@300;600;700;800&display=swap" rel="stylesheet">
<style>
  :root {
    --canvas: #ffffff;
    --navy-deep: #0a2158;
    --navy-band: #0e2c6e;
    --navy-tab: #183f86;
    --sky-light: #5fb0ee;
    --sky-mid: #2f7fd6;
    --sky-deep: #1a4fa8;
    --white: #ffffff;
    --tagline: #c8d6f0;
  }
  html, body {
    margin: 0;
    width: 1200px;
    height: 1200px;
    overflow: hidden;
    background: var(--canvas);
    font-family: "Montserrat", sans-serif;
  }
  .canvas {
    position: relative;
    width: 1200px;
    height: 1200px;
  }
  .label {
    position: absolute;
    left: 100px;
    top: 200px;
    width: 1000px;
    height: 800px;
    background: var(--navy-deep);
    overflow: hidden;
  }
  .label__top-band {
    height: 56px;
    background: var(--navy-band);
    display: flex;
    align-items: center;
    justify-content: center;
  }
  .label__servings {
    margin: 0;
    font-weight: 600;
    font-size: 22px;
    letter-spacing: 2px;
    color: var(--tagline);
    text-transform: uppercase;
  }
  .label__scene {
    position: absolute;
    top: 56px;
    left: 0;
    width: 100%;
    height: 530px;
    background:
      linear-gradient(180deg, rgba(10,33,88,0) 70%, var(--navy-deep) 100%),
      linear-gradient(160deg, var(--sky-light) 0%, var(--sky-mid) 45%, var(--sky-deep) 100%);
  }
  .brand {
    position: absolute;
    top: 300px;
    left: 0;
    width: 100%;
    text-align: center;
    margin: 0;
    font-weight: 800;
    font-size: 96px;
    letter-spacing: 2px;
    line-height: 1;
    color: var(--white);
    text-transform: uppercase;
  }
  .flavor-tab {
    position: absolute;
    top: 596px;
    left: 225px;
    width: 550px;
    height: 84px;
    background: var(--navy-tab);
    clip-path: polygon(4% 0, 100% 0, 100% 100%, 0 100%);
    display: flex;
    align-items: center;
    justify-content: center;
  }
  .flavor-tab__name {
    margin: 0;
    font-weight: 700;
    font-size: 42px;
    letter-spacing: 2px;
    color: var(--white);
    text-transform: uppercase;
  }
  .label__benefits {
    position: absolute;
    top: 698px;
    width: 100%;
    text-align: center;
    margin: 0;
    font-weight: 300;
    font-size: 26px;
    letter-spacing: 0.5px;
    color: var(--tagline);
    text-transform: uppercase;
  }
  .label__type {
    position: absolute;
    top: 740px;
    width: 100%;
    text-align: center;
    margin: 0;
    font-weight: 600;
    font-size: 28px;
    letter-spacing: 1px;
    color: var(--white);
    text-transform: uppercase;
  }
</style>
</head>
<body>
  <main class="canvas">
    <section class="label">
      <div class="label__top-band">
        <p class="label__servings">40 Servings</p>
      </div>
      <div class="label__scene" role="img" aria-label="Icy blue mountain and glacier landscape with faceted light shapes"></div>
      <h1 class="brand">Tideward Fuel</h1>
      <div class="flavor-tab">
        <h2 class="flavor-tab__name">Ember Dusk</h2>
      </div>
      <p class="label__benefits">Energy, Focus, Reaction, and Clarity</p>
      <p class="label__type">Dietary Supplement</p>
    </section>
  </main>
</body>
</html>
```